Social Media Marketing website

Need website designed for social media marketing company BrightLoop.com
Do no currently have logo.
Pages:
Main
Services
Order
Contact
Please use dummy text for now. I will provide content to winner later to add.
Main page should clearly show the steps with some sort of graphic: Establish, Engage, Analyze.
Services provided (steps):
1) Establish social media presence
2) Social media management and advertising
3) Analyze and engage
Site should be simple, clean and attractive. Design examples:
http://plinkster.com/
http://www.quillbase.com/
http://www.harrowvalemq.com/
Be creative! It should not look like a template.
Updates
Updated examples.
Contact me for questions.
dave@brightloop.com
3) Analyze and engage
Advertising

```html
<!DOCTYPE html>
<html lang="en">
<head>
<meta charset="utf-8">
<title>BrightLoop — Social Media Marketing</title>
<link href="https://fonts.googleapis.com/css2?family=Alfa+Slab+One&family=Arimo:wght@400&display=swap" rel="stylesheet">
<style>
  :root {
    --orange: #ff6a00;
    --orange-soft: #ffc766;
    --orange-deep: #ffa020;
    --ink: #333333;
    --body-text: #555555;
    --muted: #999999;
    --rule: #cccccc;
    --white: #ffffff;
  }
  * { margin: 0; padding: 0; box-sizing: border-box; }
  html, body { width: 1200px; height: 990px; overflow: hidden; background: var(--white); }
  body { position: relative; font-family: "Arimo", Arial, sans-serif; }

  .brand {
    position: absolute; left: 132px; top: 30px;
    font-family: "Alfa Slab One", serif; font-size: 29px; color: var(--orange);
  }
  .main-nav { position: absolute; top: 44px; left: 0; width: 1200px; }
  .main-nav a {
    position: absolute; font-size: 16px; color: var(--orange); text-decoration: none;
  }

  .hero-band {
    position: absolute; left: 0; top: 100px; width: 1200px; height: 380px;
  }
  .step-circle {
    position: absolute; top: 160px; width: 240px; height: 240px; border-radius: 50%;
    background: var(--white);
  }
  .step-icon { position: absolute; left: 70px; top: 22px; width: 100px; height: 110px; }
  .step-line {
    position: absolute; left: -30px; width: 300px; text-align: center; white-space: nowrap;
    font-family: "Alfa Slab One", serif; color: var(--ink); line-height: 1; letter-spacing: 0.3px;
  }
  .step-line.free { left: auto; width: auto; text-align: left; }
  .step-line .amp { font-size: 16px; }

  .feature {
    position: absolute; top: 524px; width: 262px;
  }
  .feature h2 {
    font-family: "Alfa Slab One", serif; font-weight: 400; font-size: 20px; color: var(--orange);
  }
  .feature p {
    margin-top: 20px; font-size: 12.8px; line-height: 15px; color: var(--body-text);
  }

  .cta-panel {
    position: absolute; left: 130px; top: 750px; width: 940px; height: 120px; border-radius: 8px;
    background: linear-gradient(to bottom, var(--orange-soft), var(--orange-deep));
  }
  .cta-heading {
    position: absolute; left: 22px; top: 28px; width: 120px;
    font-family: "Alfa Slab One", serif; font-size: 19px; line-height: 22px; color: var(--white);
  }
  .cta-text {
    position: absolute; left: 162px; top: 30px; width: 218px;
    font-size: 12.6px; line-height: 15px; color: var(--white);
  }
  .cta-input {
    position: absolute; left: 400px; top: 45px; width: 270px; height: 30px;
    background: var(--white); border: 1px solid var(--rule);
  }
  .cta-button {
    position: absolute; left: 700px; top: 34px; width: 200px; height: 50px; border-radius: 8px;
    background: linear-gradient(to bottom, #ffffff, #d8d8d8);
    box-shadow: 0 2px 3px rgba(0,0,0,0.25);
    font-family: "Alfa Slab One", serif; font-size: 19px; color: var(--orange);
    line-height: 50px; text-align: center;
  }

  .site-footer {
    position: absolute; left: 131px; top: 911px; width: 940px;
    border-top: 1px solid var(--rule); text-align: center;
    font-size: 11px; color: var(--muted); padding-top: 10px;
  }
</style>
</head>
<body>
  <header>
    <div class="brand">BrightLoop</div>
    <nav class="main-nav">
      <a href="#" style="left:708px">Main</a>
      <a href="#" style="left:799px">Services</a>
      <a href="#" style="left:912px">Order</a>
      <a href="#" style="left:1004px">Contact</a>
    </nav>
  </header>

  <svg class="hero-band" viewBox="0 0 1200 380" role="img" aria-label="Warm orange and yellow bubble pattern band">
    <defs>
      <linearGradient id="bandFill" x1="0" y1="0" x2="1" y2="0">
        <stop offset="0" stop-color="#ffb640"/>
        <stop offset="0.5" stop-color="#ffc95a"/>
        <stop offset="1" stop-color="#ffa62a"/>
      </linearGradient>
    </defs>
    <path fill="url(#bandFill)" d="M0 0 H1200 V360 Q1170 350 1140 362 Q1100 384 1060 366 Q1020 350 985 364 Q950 382 910 362 Q880 348 845 365 Q800 385 760 362 Q725 345 690 363 Q650 382 610 360 Q575 345 540 362 Q500 384 460 362 Q420 345 385 363 Q345 382 305 360 Q270 345 235 362 Q195 382 155 362 Q115 345 80 364 Q40 380 0 358 Z"/>
  </svg>

  <section class="steps">
    <div class="step-circle" style="left:160px">
      <svg class="step-icon" viewBox="0 0 100 110" role="img" aria-label="Globe illustration">
        <defs><radialGradient id="globeFill" cx="0.4" cy="0.35" r="0.7">
          <stop offset="0" stop-color="#6fd0f5"/><stop offset="1" stop-color="#1b7fc4"/>
        </radialGradient></defs>
        <ellipse cx="50" cy="106" rx="40" ry="4" fill="#bbbbbb"/>
        <circle cx="50" cy="54" r="50" fill="url(#globeFill)"/>
      </svg>
      <div class="step-line" style="top:147px;font-size:26px">ESTABLISH</div>
      <div class="step-line" style="top:176px;font-size:19px">SOCIAL MEDIA</div>
      <div class="step-line" style="top:198px;font-size:27px">PRESENCE</div>
    </div>

    <div class="step-circle" style="left:480px">
      <svg class="step-icon" viewBox="0 0 100 110" role="img" aria-label="Person silhouette illustration">
        <defs><linearGradient id="personFill" x1="0" y1="0" x2="0" y2="1">
          <stop offset="0" stop-color="#3a3a3a"/><stop offset="1" stop-color="#111111"/>
        </linearGradient></defs>
        <rect x="5" y="4" width="90" height="104" rx="20" fill="url(#personFill)"/>
      </svg>
      <div class="step-line" style="top:158px;font-size:26px">SOCIAL MEDIA</div>
      <div class="step-line" style="top:184px;font-size:25px">MANAGEMENT</div>
      <div class="step-line" style="top:210px;font-size:25px"><span class="amp">&amp;</span> ADVERTISING</div>
    </div>

    <div class="step-circle" style="left:812px">
      <svg class="step-icon" viewBox="0 0 100 110" aria-hidden="true">
        <ellipse cx="50" cy="104" rx="40" ry="4" fill="#bbbbbb"/>
        <path d="M50 50 L20 12 A50 50 0 0 1 89 20 Z" fill="#22b8f0"/>
        <path d="M50 50 L89 20 A50 50 0 0 1 100 50 Z" fill="#d61fb8"/>
        <path d="M50 50 L100 50 A50 50 0 0 1 88 82 Z" fill="#e4d21c"/>
        <path d="M50 50 L88 82 A50 50 0 1 1 20 12 Z" fill="#9ccf1a"/>
      </svg>
      <div class="step-line free" style="left:20px;top:167px;font-size:24px">ANALYZE</div>
      <div class="step-line free" style="left:18px;top:194px;font-size:27px">ENGAGE</div>
      <div class="step-line free" style="left:178px;top:168px;font-size:50px">&amp;</div>
    </div>
  </section>

  <section class="features">
    <article class="feature" style="left:152px">
      <h2>Title Number One</h2>
      <p>Harrowvale is designed to move people deeper into real relationships. Harrowvale automates much of the administration, for example it can automatically connect people into home groups based on your criteria, so you can spend your time in relationship not administrating.</p>
    </article>
    <article class="feature" style="left:472px">
      <h2>Another Title</h2>
      <p>Harrowvale encourages behaviors important to your local community such as connecting people to volunteer opportunities, moving people into relationship, managing events and much more.&nbsp; Harrowvale is not a social network, it is designed for the unique community needs of the local church</p>
    </article>
    <article class="feature" style="left:791px">
      <h2>One More Title</h2>
      <p>Harrowvale encourages behaviors important to your local community such as connecting people to volunteer opportunities, moving people into relationship, managing events and much more.&nbsp; Harrowvale is not a social network, it is designed for the unique community needs of the local church</p>
    </article>
  </section>

  <section class="cta-panel">
    <div class="cta-heading">Want to Find Out More?</div>
    <p class="cta-text">Interested in using this powerful tool to help your community?&nbsp; Demo Harrowvale and see how it can help you be the church</p>
    <div class="cta-input"></div>
    <div class="cta-button">Call to action</div>
  </section>

  <footer class="site-footer">Copyright 2011. BrightLoop</footer>
</body>
</html>
```